Web Based Ordering. We have an existing input screen- Need to Clean it up

we have an existing ordering Modal on a trucking management system, but it looks and feels clunky. We would like to modernize the look and feel of it. We need to keep the same input fields, but we are open to any type of reconfiguration or layout changes you can think of to improve the flow and layout.

This design is for a web browser, not mobile app.

Target Market(s)

construction and trucking industry

Colors
85acd3
3176b5
33a6d7
85cae6
33b8a4
86cfc6

Requirements
Must have
• all the input fields displayed are required
Nice to have
• some of the fields can probably be combined to consolidate the number of tabs.

```html
<!DOCTYPE html>
<html lang="en">
<head>
<meta charset="utf-8">
<title>New Material Order – Order Flow Screens</title>
<link href="https://fonts.googleapis.com/css2?family=Poppins:wght@400;500;600;700&display=swap" rel="stylesheet">
<style>
  :root{
    --brand:#1b94dc;
    --brand-dark:#1580c2;
    --page:#ececec;
    --panel:#f7f7f9;
    --card:#ffffff;
    --ink:#1c1c1c;
    --muted:#8c8f96;
    --line:#e3e5ea;
    --chip:#e9ebef;
  }
  *{box-sizing:border-box;margin:0;padding:0}
  html,body{width:1200px;height:976px;overflow:hidden}
  body{background:var(--page);font-family:"Poppins",sans-serif;color:var(--ink)}
  .board{display:grid;grid-template-columns:repeat(3,380px);grid-template-rows:repeat(2,472px);gap:10px 15px;padding:11px 15px}
  .panel{background:var(--panel);display:flex;flex-direction:column;box-shadow:0 4px 14px rgba(0,0,0,.12);overflow:hidden;position:relative}
  .panel--wide{grid-column:span 2}
  .bar{background:var(--brand);color:#fff;font-size:7px;font-weight:600;padding:4px 0 4px 32px}
  .steps{display:flex;align-items:center;gap:3px;padding:10px 32px;background:#fff;position:relative}
  .step{font-size:4.6px;color:#555;background:var(--chip);border-radius:6px;padding:2px 4px;white-space:nowrap}
  .step.is-active{background:var(--brand);color:#fff}
  .edit{position:absolute;right:30px;top:9px;width:8px;height:8px}
  .body{flex:1;display:flex;flex-direction:column;align-items:center;padding:26px 76px 0}
  .title{font-size:16px;font-weight:700;margin-bottom:16px}
  .row{display:flex;gap:12px;width:100%;margin-bottom:9px}
  .field{flex:1;min-width:0;display:flex;flex-direction:column;gap:3px}
  .label{font-size:4.4px;color:var(--muted);white-space:nowrap}
  .input{height:11px;background:#fff;border:1px solid var(--line);border-radius:6px;font-size:4.4px;color:#555;display:flex;align-items:center;justify-content:space-between;padding:0 6px;white-space:nowrap;overflow:hidden}
  .input .caret{color:#aaa}
  .pill{font-size:4.4px;color:#fff;background:var(--brand);border-radius:6px;padding:2px 6px;margin:2px 0 10px}
  .photo{border-radius:6px;background:linear-gradient(135deg,#c7d3dc,#8aa2b2 55%,#dfe6ea)}
  .photo--round{width:72px;height:72px;border-radius:50%;margin:22px 0}
  .photo--rect{width:112px;height:68px;margin:14px 0}
  .continue{width:102px;height:17px;border-radius:9px;background:var(--brand);color:#fff;font-size:6px;font-weight:500;display:flex;align-items:center;justify-content:center;box-shadow:0 2px 5px rgba(27,148,220,.35);margin-top:auto}
  .cancel{font-size:4.4px;color:var(--muted);margin:6px 0 14px}
  .foot{border-top:1px solid var(--brand);font-size:4.4px;color:var(--muted);text-align:center;padding:5px 0 6px;background:#fff}
  .toggle{display:flex;gap:2px;justify-content:center}
  .toggle span{font-size:4.4px;padding:1px 3px;border-radius:4px;background:var(--chip);color:#555}
  .toggle .on{background:var(--brand);color:#fff}
  .center-label{text-align:center;font-size:4.4px;color:var(--muted);margin-bottom:5px}
  .chips{display:flex;gap:6px;width:100%;margin-bottom:10px}
  .chip{flex:1;height:12px;border-radius:6px;background:var(--chip);font-size:4.4px;color:#777;display:flex;align-items:center;padding-left:6px}
  .chip.is-active{background:var(--brand);color:#fff}
  .counter{display:flex;align-items:center;gap:4px;font-size:4.4px;color:#555;white-space:nowrap}
  .btn-sq{width:6px;height:6px;border-radius:2px;background:var(--brand);color:#fff;font-size:5px;line-height:6px;text-align:center}
  .quick{background:var(--brand);color:#fff;border-radius:4px;padding:1px 4px;font-size:4.2px}
  .textarea{height:46px;background:#fff;border:1px solid var(--line);border-radius:6px;font-size:4.4px;color:#555;padding:5px 6px}
  .hero{position:absolute;left:0;right:0;top:14px;height:170px;background:linear-gradient(180deg,#bcd9ec 0%,#d8e4ea 35%,#9fa98c 62%,#6f7d6a 100%)}
  .steps--over{background:transparent;z-index:1}
  .truck-art{position:absolute;left:50%;top:38px;transform:translateX(-50%);width:88px;height:130px;border-radius:8px;background:linear-gradient(180deg,#f4f4f4,#cfd3d6);z-index:2}
  .summary-card{position:relative;z-index:1;margin:120px 60px 12px;background:var(--card);border-radius:12px;box-shadow:0 4px 14px rgba(0,0,0,.08);padding:40px 40px 14px;display:flex;flex-direction:column;align-items:center;flex:1}
  .summary-card .title{font-size:17px;margin-bottom:14px}
  .facts{display:grid;grid-template-columns:repeat(4,1fr);gap:12px 20px;width:100%;margin-bottom:18px}
  .fact dt{font-size:5px;font-weight:600;margin-bottom:3px}
  .fact dd{font-size:4.4px;color:#666;line-height:1.5}
  .fact dd.accent{color:var(--brand)}
  .place{width:140px;height:18px;border-radius:9px;background:var(--brand);color:#fff;font-size:6.5px;display:flex;align-items:center;justify-content:center}
</style>
</head>
<body>
<div class="board">

  <section class="panel">
    <header class="bar">New Material Order</header>
    <nav class="steps">
      <span class="step is-active">Date and Start</span><span class="step">Destination</span><span class="step">Material</span><span class="step">Trucks</span><span class="step">Rates</span><span class="step">Summary</span>
      <svg class="edit" viewBox="0 0 10 10"><path d="M1 9l1-3 5-5 2 2-5 5z" fill="var(--brand)"/></svg>
    </nav>
    <main class="body">
      <h2 class="title">Date and Start</h2>
      <div class="row"><div class="field"><span class="label">Customer *</span><div class="input">Ridgeline Paving Company, Inc.<span class="caret">× ⌄</span></div></div></div>
      <div class="row"><div class="field"><span class="label">Starting Location *</span><div class="input">Yard 7 North Site 3<span class="caret">× ⌄</span></div></div></div>
      <div class="row">
        <div class="field"><span class="label">Load Date *</span><div class="input">02/27/2021<span class="caret">▢</span></div></div>
        <div class="field"><span class="label">Load Time *</span><div class="input">6:00 AM</div></div>
      </div>
      <div class="photo photo--round" role="img" aria-label="White semi truck with trailer"></div>
      <div class="continue">Continue</div>
      <div class="cancel">Cancel</div>
    </main>
    <footer class="foot">Copyright © 2021. All rights reserved.</footer>
  </section>

  <section class="panel">
    <header class="bar">New Material Order</header>
    <nav class="steps">
      <span class="step">Date and Start</span><span class="step is-active">Destination</span><span class="step">Material</span><span class="step">Trucks</span><span class="step">Rates</span><span class="step">Summary</span>
      <svg class="edit" viewBox="0 0 10 10"><path d="M1 9l1-3 5-5 2 2-5 5z" fill="var(--brand)"/></svg>
    </nav>
    <main class="body">
      <h2 class="title">Destination</h2>
      <div class="row">
        <div class="field"><span class="label">P.O. / Job #</span><div class="input">12</div></div>
        <div class="field"><span class="label">Destination *</span><div class="input">RPC Plant 12 Mill...<span class="caret">⌄</span></div></div>
      </div>
      <div class="row"><div class="field"><span class="label">Address *</span><div class="input">1480 Quarry Industrial Parkway, Millbrook, GA, 30100</div></div></div>
      <div class="row">
        <div class="field"><span class="label">Job Site Contact *</span><div class="input">Dana Keller<span class="caret">× ⌄</span></div></div>
        <div class="field"><span class="label">Contact Number *</span><div class="input">(555) 014-2290</div></div>
      </div>
      <span class="pill">+ Add Second Destination</span>
      <div class="row">
        <div class="field"><span class="label">Billing Job Site *</span><div class="input">Yard 7 North Site 3<span class="caret">⌄</span></div></div>
        <div class="field"><span class="label">Phase Code</span><div class="input">51 015, 1102 Ra...<span class="caret">× ⌄</span></div></div>
      </div>
      <span class="label">Providing Ringer?</span>
      <div class="toggle" style="margin-top:3px"><span>Yes</span><span class="on">No</span></div>
      <div class="continue">Continue</div>
      <div class="cancel">Cancel</div>
    </main>
    <footer class="foot">Copyright © 2021. All rights reserved.</footer>
  </section>

  <section class="panel">
    <header class="bar">New Material Order</header>
    <nav class="steps">
      <span class="step">Date and Start</span><span class="step">Destination</span><span class="step is-active">Material</span><span class="step">Trucks</span><span class="step">Rates</span><span class="step">Summary</span>
      <svg class="edit" viewBox="0 0 10 10"><path d="M1 9l1-3 5-5 2 2-5 5z" fill="var(--brand)"/></svg>
    </nav>
    <main class="body">
      <h2 class="title">Material</h2>
      <div class="row"><div class="field"><span class="label">Work Type *</span><div class="input">Asphalt Machine Paving</div></div></div>
      <div class="row">
        <div class="field"><span class="label">Material Type *</span><div class="input">12.5mm PEM<span class="caret">× ⌄</span></div></div>
        <div class="field"><span class="label">Tonnage *</span><div class="input">400<span class="caret">⇕</span></div></div>
      </div>
      <span class="pill">+ Additional Material</span>
      <div class="photo photo--rect" role="img" aria-label="Row of parked trucks"></div>
      <div class="continue">Continue</div>
      <div class="cancel">Cancel</div>
    </main>
    <footer class="foot">Copyright © 2021. All rights reserved.</footer>
  </section>

  <section class="panel">
    <header class="bar">New Material Order</header>
    <nav class="steps">
      <span class="step">Date and Start</span><span class="step">Destination</span><span class="step">Material</span><span class="step is-active">Trucks</span><span class="step">Rates</span><span class="step">Summary</span>
      <svg class="edit" viewBox="0 0 10 10"><path d="M1 9l1-3 5-5 2 2-5 5z" fill="var(--brand)"/></svg>
    </nav>
    <main class="body" style="padding-left:40px;padding-right:40px">
      <h2 class="title">Trucks</h2>
      <div class="center-label">Acceptable Truck Types *</div>
      <div class="chips"><span class="chip">Trailer Dump</span><span class="chip">Quad</span><span class="chip is-active">18 Wheel (Tandem)</span><span class="chip">Rough 15</span></div>
      <div class="row"><div class="field"><span class="label">Trucks Required *</span><div class="input">12<span class="caret">⇕</span></div></div></div>
      <div class="row" style="justify-content:space-between">
        <div class="field"><span class="label">Delay Between Trucks</span><div class="counter"><span class="btn-sq">−</span>5 minutes<span class="btn-sq">+</span></div></div>
        <div class="field"><span class="label">Quick Select</span><div class="counter"><span class="quick">15 min · 30 min · 45 min</span></div></div>
        <div class="field"><span class="label">Trucks at First Interval</span><div class="counter"><span class="btn-sq">−</span>1<span class="btn-sq">+</span></div></div>
        <div class="field"><span class="label">Trucks at Later Times</span><div class="counter"><span class="btn-sq">−</span>1<span class="btn-sq">+</span></div></div>
      </div>
      <div class="row"><div class="field"><span class="label">Dispatch Instructions</span><div class="textarea">dispatch instructions go here</div></div></div>
      <div class="continue">Continue</div>
      <div class="cancel">Cancel</div>
    </main>
    <footer class="foot">Copyright © 2021. All rights reserved.</footer>
  </section>

  <section class="panel panel--wide">
    <header class="bar">New Material Order</header>
    <div class="hero" role="img" aria-label="Mountain highway at sunrise"></div>
    <nav class="steps steps--over">
      <span class="step">Date and Start</span><span class="step">Destination</span><span class="step">Material</span><span class="step">Trucks</span><span class="step">Rates</span><span class="step is-active">Summary</span>
      <svg class="edit" viewBox="0 0 10 10"><path d="M1 9l1-3 5-5 2 2-5 5z" fill="var(--brand)"/></svg>
    </nav>
    <div class="truck-art" role="img" aria-label="White truck cab, front view"></div>
    <div class="summary-card">
      <h2 class="title">Summary</h2>
      <dl class="facts">
        <div class="fact"><dt>Date</dt><dd>Sat, Feb 27 at 6:00 AM</dd></div>
        <div class="fact"><dt>Billing Job Site</dt><dd>Yard 7 North Site 3</dd></div>
        <div class="fact"><dt>Trucks Required</dt><dd>12</dd></div>
        <div class="fact"><dt>Start Location</dt><dd>Yard 7 North Site 3</dd></div>
        <div class="fact"><dt>Destination</dt><dd>RPC Plant 12 Millbrook<br>(PO / Job#12)</dd></div>
        <div class="fact"><dt>Phase Code</dt><dd>51 015</dd></div>
        <div class="fact"><dt>Dispatch Instructions</dt><dd>dispatch instructions go here</dd></div>
        <div class="fact"><dt>Work Type</dt><dd>Asphalt Machine Paving</dd></div>
        <div class="fact"><dt>Material</dt><dd>12.5mm PEM – 400 tons</dd></div>
        <div class="fact"><dt>Truck Types</dt><dd>18 Wheel (Tandem)</dd></div>
        <div class="fact"><dt>Price Per Ton</dt><dd class="accent">18 Wheel (Tandem)<br>at $3.50/ton</dd></div>
        <div class="fact"><dt>Time Delay</dt><dd>5 minutes</dd></div>
      </dl>
      <div class="place">Place Order</div>
      <div class="cancel" style="margin-bottom:0">Cancel</div>
    </div>
    <footer class="foot">Copyright © 2021. All rights reserved.</footer>
  </section>

</div>
</body>
</html>
```